DL Flyer for vehicle buying/selling service and advice business

New business to help people sell their current vehicle then select and buy and maintain their next car. (New or used).
We'll prepare and sell your car for you and get $,000s more than a trade in.
Offer advice as to the best car currently on the market based on our customer's needs.
With country wide sourcing network of cars across all manufacturers we have great buying power to ensure the very best possible price.
Personal service, including preparation of car for sale, pickup of old and drop-off of new vehicles, organise RWC and any required repairs.
We are NOT a car dealer so we WILL not try to sell you the vehicles we own.
Totally impartial, professional and friendly service making the purchase of your next car a great experience.

Flyer wording===========“Don’t sell your car or buy your next car without speaking to us”We guarantee to get you a better price for your current car and to find a cheaper purchase price for your next car.With a country wide sourcing network of cars “new and used” across all manufacturers we have sensational buying power to ensure the very best possible price.We can source the right car on any budget, from $2,000 to $200,000We are NOT a car dealer so we WILL not try to sell you the vehicles we own.By not being affiliated with any individual car manufacturer or dealer we can offer absolute impartiality.We’ll sit with you to discuss the best car for your needs and even bring the car to you for a test drive without the pressure of a salesperson nearby.Our services include:• Selling your current car: - Obtaining a roadworthy certificate - Organising any repairs needed - Detailing your car (wash, vacuum, polish) - Advertising of your car - Dealing with potential buyers - Negotiating the best price on your behalf• Assisting with the selection of your next car• Organising test drives• Purchasing the car of your choice - Sourcing the very best price• Ongoing management of their vehicle (service, clean, repair)Possible inclusions in the flyer might be:Advantages of upgrading to a new vehicle include:o reliability, o safety,o fuel efficiencyo comfort.Space for a couple of short testimonials Background images of all of the major car manufacturers Added Friday, July 29, 2016

Target Market(s)

Local community.
Initially will drop DL flyers in local post boxes

Industry/Entity Type

Business

Requirements
Must have
• Flyer wording:
• ===========
• “Don’t sell your car or buy your next car without speaking to us”
• ---------------------------------------------------------------------------------
• We guarantee to get you a better price for your current car and to find a cheaper purchase price for your next car.
• With a country wide sourcing network of cars “new and used” across all manufacturers we have sensational buying power to ensure the very best possible price.
• We can source the right car on any budget, from $2,000 to $200,000
• We are NOT a car dealer so we WILL not try to sell you the vehicles we own.
• By not being affiliated with any individual car manufacturer or dealer we can offer absolute impartiality.
• We’ll sit with you to discuss the best car for your needs and even bring the car to you for a test drive without the pressure of a salesperson nearby.
• Our services include:
• • Selling your current car:
• o Obtaining a roadworthy certificate
• o Organising any repairs needed
• o Detailing your car (wash, vacuum, polish)
• o Advertising of your car
• o Dealing with potential buyers
• o Negotiating the best price on your behalf
• • Assisting with the selection of your next car
• • Organising test drives
• • Purchasing the car of your choice
• o Sourcing the very best price
• • Ongoing management of your vehicle (service, clean, repair)
• Call Gregor on: 0438 215064
Nice to have
• Possible inclusions on the flyer might be:
• List of advantages of upgrading to a new vehicle:
• o reliability,
• o safety,
• o fuel efficiency
• o comfort
• Space for a couple of short testimonials
• Background images of all of the major car manufacturers

```html
<!DOCTYPE html>
<html lang="en">
<head>
<meta charset="utf-8">
<title>KVB Vehicle Brokerage – DL Flyer</title>
<link href="https://fonts.googleapis.com/css2?family=Oswald:wght@500&family=Open+Sans:wght@700&family=Source+Sans+3:ital,wght@0,400;0,600;1,400&display=swap" rel="stylesheet">
<style>
:root{
  --orange:#f26f21;
  --charcoal:#48484a;
  --ink:#333336;
  --paper:#ffffff;
  --mist:#f1f1f1;
  --rule:#bdbdbd;
}
*{box-sizing:border-box;margin:0;padding:0}
html,body{width:1200px;height:989px;overflow:hidden;background:#e6e4e1}
body{position:relative;font-family:"Source Sans 3",Arial,sans-serif}
.flyer{position:absolute;width:394px;height:827px;background:var(--charcoal);overflow:hidden;transform:scale(.923);transform-origin:0 0;box-shadow:0 3px 10px rgba(0,0,0,.25)}
.flyer--front{left:209px;top:91px}
.flyer--back{left:634px;top:147px}
.shapes{position:absolute;inset:0}
.abs{position:absolute}
.wordmark{font-family:"Open Sans",Arial,sans-serif;font-weight:700;font-size:46px;letter-spacing:9px;line-height:1}
.front-brand{left:28px;top:8px;color:var(--ink)}
.front-tagline{left:163px;top:10px;font-size:14.5px;line-height:19px;color:var(--ink);text-transform:uppercase}
.front-photo{left:0;top:0;width:394px;height:827px;pointer-events:none}
.badge{left:254px;top:227px;width:116px;height:116px;border-radius:50%;background:var(--charcoal);border:3px solid var(--orange);box-shadow:0 2px 5px rgba(0,0,0,.4);display:flex;align-items:center;justify-content:center;text-align:center;font-family:Oswald,sans-serif;font-size:10px;line-height:14px;color:#fff;text-transform:uppercase}
.hi{color:var(--orange)}
.headline{left:0;width:394px;top:350px;text-align:center;font-family:Oswald,sans-serif;font-size:15.5px;line-height:22px;color:var(--orange);text-transform:uppercase}
.checks{left:18px;top:414px;width:362px;list-style:none}
.checks li{position:relative;padding-left:16px;font-size:10px;line-height:12px;color:#fff;text-align:justify;margin-bottom:7px}
.checks li::before{content:"";position:absolute;left:3px;top:1px;width:4px;height:7px;border:solid var(--orange);border-width:0 2px 2px 0;transform:rotate(40deg)}
.tab{height:24px;background:var(--orange);color:#fff;font-family:Oswald,sans-serif;font-size:14px;line-height:24px;text-transform:uppercase;border-radius:0 12px 12px 0;white-space:nowrap}
.advantages-tab{left:0;top:593px;padding:0 14px 0 16px;font-size:12px;letter-spacing:-.1px}
.advantages{left:14px;top:622px;width:240px;list-style:none;display:grid;grid-template-columns:108px 120px;row-gap:2px}
.advantages li,.services li{position:relative;padding-left:16px;color:#fff}
.advantages li{font-size:13px;line-height:16px}
.dot::before{content:"";position:absolute;left:0;top:4px;width:9px;height:9px;border-radius:50%;background:var(--orange)}
.dot::after{content:"";position:absolute;left:2px;top:6.5px;width:3px;height:3px;border:solid #fff;border-width:1px 1px 0 0;transform:rotate(45deg)}
.photo-disc{border-radius:50%;border:3px solid var(--orange);box-shadow:0 2px 5px rgba(0,0,0,.35)}
.disc-engine{left:18px;top:666px;width:94px;height:94px;background:radial-gradient(circle at 40% 40%,#c9c9c9,#5b5b5b 70%,#2d2d2d)}
.disc-polish{left:106px;top:698px;width:66px;height:66px;background:radial-gradient(circle at 45% 50%,#d86a3a,#6c3b2b 55%,#2c2c2c)}
.service-tab{left:274px;top:690px;width:120px;height:20px;line-height:20px;font-size:11px;border-radius:10px 0 0 10px;padding-left:30px}
.service-note{right:9px;top:713px;width:220px;text-align:right;font-size:12px;line-height:14.5px;color:#fff}
.call-front{left:21px;top:764px;font-size:15px;line-height:18px;color:var(--ink);font-weight:600}
.phone{color:var(--orange);white-space:nowrap}
.phone svg{width:12px;height:12px;vertical-align:-1px;margin-right:3px}
.back-brand{left:260px;top:310px;color:#fff}
.services-tab{left:0;top:370px;width:180px;padding-left:18px;font-size:15px}
.services{left:14px;top:408px;width:372px;list-style:none}
.services > li{font-size:14px;line-height:19px}
.sub{display:grid;grid-template-columns:187px 180px;list-style:none;margin:1px 0 6px -16px}
.sub li{font-size:9.5px;line-height:13.5px;color:#fff;padding-left:0}
.sub li::before{content:"• "}
.sub--single{grid-template-columns:1fr;margin-left:-2px}
.quote{left:14px;top:596px;width:366px;text-align:center;font-style:italic;font-size:11.5px;line-height:12.5px;color:#e8e8e8}
.call-box{left:48px;top:658px;width:295px;height:52px;border:2px solid var(--orange);border-radius:10px;text-align:center;color:#fff;font-size:17.5px;line-height:20px;font-weight:600;padding-top:5px}
.maker-strip{left:0;top:727px;width:394px;height:100px;background:var(--paper);border-top:5px solid var(--orange);display:grid;grid-template-columns:repeat(13,1fr);align-items:center;justify-items:center;padding:6px 6px}
.maker{width:20px;height:20px;border-radius:50%;border:2px solid var(--rule);background:var(--mist)}
</style>
</head>
<body>

<article class="flyer flyer--front">
  <svg class="shapes" viewBox="0 0 394 827" aria-hidden="true">
    <rect width="394" height="92" fill="#fff"/>
    <path d="M0 92 Q200 40 394 78 L394 92 Q200 58 0 106 Z" fill="var(--orange)"/>
    <path d="M0 304 Q110 270 394 238 L394 290 Q220 300 0 345 Z" fill="var(--orange)"/>
    <path d="M0 680 Q130 690 210 760 Q290 822 394 780 L394 827 L0 827 Z" fill="var(--mist)"/>
    <path d="M230 772 Q300 815 394 760 L394 780 Q300 826 230 772 Z" fill="var(--orange)"/>
  </svg>
  <svg class="abs front-photo" viewBox="0 0 394 827" role="img" aria-label="Photo of a smiling woman in a car window holding up new car keys">
    <defs>
      <linearGradient id="frontPhoto" x1="0" y1="0" x2="1" y2="1">
        <stop offset="0" stop-color="#6e6358"/>
        <stop offset=".45" stop-color="#d9c6a8"/>
        <stop offset="1" stop-color="#e9e9ea"/>
      </linearGradient>
    </defs>
    <path d="M0 106 Q200 58 394 92 L394 240 Q110 272 0 306 Z" fill="url(#frontPhoto)"/>
  </svg>
  <div class="abs wordmark front-brand">KVB</div>
  <p class="abs front-tagline">New (full service) vehicle<br>brokerage business</p>
  <div class="abs badge"><p>We are <span class="hi">not</span> a<br>car dealer<br>so we <span class="hi">will</span> not<br>try to sell you the<br>vehicles we own</p></div>
  <h1 class="abs headline">Don’t sell your car or buy your next car<br>without speaking to us</h1>
  <ul class="abs checks">
    <li>We guarantee to get you a better price for your current car and to find a cheaper purchase price for your next car.</li>
    <li>With a country wide sourcing network of cars “new and used” across all manufacturers we have sensational buying power to ensure the very best possible price.</li>
    <li>We can source the right car on any budget, from $2,000 to $200,000</li>
    <li>We are NOT a car dealer so we WILL not try to sell you the vehicles we own.</li>
    <li>By not being affiliated with any individual car manufacturer or dealer we can offer absolute impartiality.</li>
    <li>We’ll sit with you to discuss the best car for your needs and even bring the car to you for a test drive without the pressure of a salesperson nearby.</li>
  </ul>
  <h2 class="abs tab advantages-tab">List of advantages of upgrading to a new vehicle</h2>
  <ul class="abs advantages">
    <li class="dot">Reliability</li><li class="dot">Fuel Efficiency</li>
    <li class="dot">Safety</li><li class="dot">Comfort</li>
  </ul>
  <div class="abs photo-disc disc-engine" role="img" aria-label="Photo of hands working on a car engine"></div>
  <div class="abs photo-disc disc-polish" role="img" aria-label="Photo of a car being polished"></div>
  <h3 class="abs tab service-tab">KVB Full Service</h3>
  <p class="abs service-note">Professional and friendly service<br>making the purchase<br>of your next car a great experience.</p>
  <p class="abs call-front">Call Gregor on<br><span class="phone"><svg viewBox="0 0 24 24"><path fill="currentColor" d="M6.6 10.8a15 15 0 0 0 6.6 6.6l2.2-2.2c.3-.3.7-.4 1-.2 1.1.4 2.3.6 3.6.6.6 0 1 .4 1 1V20c0 .6-.4 1-1 1A17 17 0 0 1 3 4c0-.6.4-1 1-1h3.5c.6 0 1 .4 1 1 0 1.3.2 2.5.6 3.6.1.3 0 .7-.2 1z"/></svg>0438 215064</span><br>to discuss your requirements</p>
</article>

<article class="flyer flyer--back">
  <svg class="shapes" viewBox="0 0 394 827">
    <defs>
      <linearGradient id="backPhoto" x1="0" y1="0" x2="0" y2="1">
        <stop offset="0" stop-color="#8e9a78"/>
        <stop offset=".5" stop-color="#d8d4cc"/>
        <stop offset="1" stop-color="#7f7a70"/>
      </linearGradient>
    </defs>
    <path d="M0 0 H394 V270 Q230 285 120 310 Q60 322 0 310 Z" fill="url(#backPhoto)" role="img" aria-label="Photo of grandparents, two girls and a dog sitting in the open boot of a car"/>
    <path d="M0 300 Q60 322 140 305 Q260 280 394 282 L394 300 Q250 296 150 322 Q60 345 0 340 Z" fill="var(--orange)" aria-hidden="true"/>
  </svg>
  <div class="abs wordmark back-brand">KVB</div>
  <h2 class="abs tab services-tab">Services we provide</h2>
  <ul class="abs services">
    <li class="dot">Selling your current car:
      <ul class="sub">
        <li>Obtaining a roadworthy certificate</li><li>Advertising of your car</li>
        <li>Organising any repairs needed</li><li>Dealing with potential buyers</li>
        <li>Detailing your car (wash, vacuum, polish)</li><li>Negotiating the best price on your behalf</li>
      </ul>
    </li>
    <li class="dot">Assisting with the selection of your next car</li>
    <li class="dot">Organising test drives</li>
    <li class="dot">Purchasing the car of your choice
      <ul class="sub sub--single"><li>Sourcing the very best price</li></ul>
    </li>
    <li class="dot">Ongoing management of your vehicle (service, clean, repair)</li>
  </ul>
  <blockquote class="abs quote">“Thanks Gregor for your wonderful advice! You take the hard work out<br>of buying a car for people like me, who know nothing<br>about cars and I am very grateful for your help.”<br>- Rosalind</blockquote>
  <p class="abs call-box">Call Gregor on <span class="phone"><svg viewBox="0 0 24 24"><path fill="currentColor" d="M6.6 10.8a15 15 0 0 0 6.6 6.6l2.2-2.2c.3-.3.7-.4 1-.2 1.1.4 2.3.6 3.6.6.6 0 1 .4 1 1V20c0 .6-.4 1-1 1A17 17 0 0 1 3 4c0-.6.4-1 1-1h3.5c.6 0 1 .4 1 1 0 1.3.2 2.5.6 3.6.1.3 0 .7-.2 1z"/></svg>0438 215064</span><br>to discuss your requirements</p>
  <div class="abs maker-strip" aria-label="Car manufacturers we source from">
    <span class="maker"></span><span class="maker"></span><span class="maker"></span><span class="maker"></span><span class="maker"></span><span class="maker"></span><span class="maker"></span><span class="maker"></span><span class="maker"></span><span class="maker"></span><span class="maker"></span><span class="maker"></span><span class="maker"></span>
    <span class="maker"></span><span class="maker"></span><span class="maker"></span><span class="maker"></span><span class="maker"></span><span class="maker"></span><span class="maker"></span><span class="maker"></span><span class="maker"></span><span class="maker"></span><span class="maker"></span><span class="maker"></span><span class="maker"></span>
    <span class="maker"></span><span class="maker"></span><span class="maker"></span><span class="maker"></span><span class="maker"></span><span class="maker"></span><span class="maker"></span><span class="maker"></span><span class="maker"></span><span class="maker"></span><span class="maker"></span><span class="maker"></span><span class="maker"></span>
  </div>
</article>

</body>
</html>
```